Banner for construction site to identify developer

we need a 4 foot by 8 foot banner to hang on the fence of a residential townhome development in Phoenix, Arizona that identifies Tolvane Holdings as the company behind the development/project. Also needs to include the logo, phone number, and web address. Would like to stick with the blue colors provided in the attached logo. The blues should stay the same but the letters in the logo can change to another color if necessary. Feel free to use "Tolvane Holdings" in place of "Tolvane Holdings Group". Looking for use of colors/design to take up space so banner is not just text with a logo.

Target Market(s)

drive by traffic looking at the site

Industry/Entity Type

Real Estate

Colors
0054AA
0677BA
7BADD7
CADEEF
E8F1F8

Requirements
Must have
• company name, phone number and web address

```html
<!DOCTYPE html>
<html lang="en">
<head>
<meta charset="utf-8">
<title>Tolvane Holdings – Site Banner</title>
<link rel="stylesheet" href="https://fonts.googleapis.com/css2?family=Open+Sans:wght@400;700;800&display=swap">
<style>
  :root {
    --backdrop: #c4c4c4;
    --banner-white: #ffffff;
    --dark: #3a3a3d;
    --dark-deep: #2e2e31;
    --ink: #36363a;
    --ribbon-blue: #1f70a4;
    --accent-blue: #1ea6e0;
    --divider: #cfcfcf;
  }
  * { box-sizing: border-box; margin: 0; padding: 0; }
  html, body {
    width: 913px; height: 1200px; overflow: hidden;
    background: var(--backdrop);
    font-family: "Open Sans", Arial, sans-serif;
  }
  .banner {
    position: absolute; left: 26px; top: 385px;
    width: 860px; height: 430px;
    background: var(--banner-white);
    box-shadow: 6px 10px 18px rgba(0,0,0,0.35);
    overflow: hidden;
  }
  .banner__photo {
    position: absolute; left: 0; top: 0; width: 100%; height: 230px;
    background:
      linear-gradient(180deg, rgba(46,46,49,0.55) 0%, rgba(46,46,49,0) 40%),
      linear-gradient(90deg, #3c3c40 0%, #48484c 35%, #424246 65%, #3a3a3d 100%);
  }
  .banner__headline {
    position: absolute; left: 0; right: 0; top: 18px;
    text-align: center; color: var(--banner-white);
    font-weight: 800; font-size: 78px; letter-spacing: -1px; line-height: 1.2;
  }
  .ribbon {
    position: absolute; left: 80px; top: 174px; width: 686px; height: 106px;
    filter: drop-shadow(0 9px 7px rgba(0,0,0,0.28));
  }
  .ribbon svg { position: absolute; inset: 0; }
  .ribbon__text {
    position: absolute; inset: 0; display: flex; flex-direction: column;
    align-items: center; justify-content: center; color: var(--banner-white);
    font-weight: 800; line-height: 1.05; padding-top: 2px;
  }
  .ribbon__lead { font-size: 40px; letter-spacing: 0.5px; }
  .ribbon__sub { font-size: 26px; letter-spacing: 0.2px; }
  .brand {
    position: absolute; left: 44px; top: 318px; display: flex; align-items: flex-end; gap: 10px;
  }
  .brand__mark { width: 30px; height: 30px; background: var(--accent-blue); margin-bottom: 22px; }
  .brand__name { color: var(--ink); font-weight: 700; font-size: 23px; line-height: 1.1; text-align: right; letter-spacing: -0.3px; }
  .divider { position: absolute; left: 333px; top: 298px; width: 1px; height: 98px; background: var(--divider); }
  .contact { position: absolute; left: 350px; right: 40px; top: 298px; }
  .contact__phone {
    display: flex; align-items: center; gap: 8px;
    color: var(--ink); font-weight: 800; font-size: 48px; line-height: 1.05; letter-spacing: -0.5px;
  }
  .contact__phone svg { flex: none; }
  .contact__web {
    margin-top: 4px; color: var(--ink); font-weight: 800; font-size: 29px; letter-spacing: 1.2px; text-align: right;
  }
  .contact__web-core { color: var(--accent-blue); }
</style>
</head>
<body>
  <section class="banner">
    <div class="banner__photo" role="img" aria-label="Dark toned photograph of a row of two-storey residential townhomes"></div>
    <h1 class="banner__headline">Tolvane Holdings</h1>

    <div class="ribbon">
      <svg width="686" height="106" viewBox="0 0 686 106" aria-hidden="true">
        <polygon points="0,0 686,0 638,106 48,106" fill="var(--ribbon-blue)"/>
      </svg>
      <div class="ribbon__text">
        <span class="ribbon__lead">CRAFTING PHOENIX'S</span>
        <span class="ribbon__sub">PREMIUM RESIDENTIAL TOWNHOMES</span>
      </div>
    </div>

    <div class="brand">
      <span class="brand__mark"></span>
      <span class="brand__name">Tolvane Holdings<br>Group</span>
    </div>

    <div class="divider"></div>

    <div class="contact">
      <div class="contact__phone">
        <svg width="40" height="40" viewBox="0 0 40 40" aria-hidden="true">
          <circle cx="20" cy="20" r="20" fill="var(--accent-blue)"/>
          <path d="M13 11c1-1 2.5-1 3.3 0l2.2 3c.7 1 .5 2.2-.4 3l-1.3 1.1c1 2.3 2.8 4.1 5.1 5.1l1.1-1.3c.8-.9 2-1.1 3-.4l3 2.2c1 .8 1 2.3 0 3.3l-1.4 1.4c-1.4 1.4-3.6 1.7-5.4.8-4.7-2.3-8.4-6-10.7-10.7-.9-1.8-.6-4 .8-5.4z" fill="#fff"/>
          <path d="M22 10a8 8 0 0 1 8 8M22 14a4 4 0 0 1 4 4" stroke="#fff" stroke-width="1.8" fill="none" stroke-linecap="round"/>
        </svg>
        <span>234 5678 4410</span>
      </div>
      <div class="contact__web">www.<span class="contact__web-core">Tolvaneholdings</span>.com</div>
    </div>
  </section>
</body>
</html>
```